Bright Pelvic Health Business Card

Need a business card for a surgical practice called Bright Pelvic Health. We have recently selected a logo (attached). The business card will need to have two formats:
1) One with the logo/physician name/ contact info on the front and location information on the back.
2) One in "appointment reminder card" style with the logo/ contact info/ date/ time on the front and the location information on the back.

The front side should include the following information:
- Logo
- Ravi K. Desai, MD FACOG
- phone: 469-555-0182
- fax: 1-469-555-0147
- email: admin@brightpelvic.example
- website: www.brightpelvichealth.example

The back side should have the office locations listed:
4812 Quarry Bend Dr, Plano, TX 75093
3650 Wrenfield Rd, Plano, TX 75025
2245 Brambleton Ln, Irving, TX 75038
915 S Garnet Ave B314, Dallas, TX 75201
1836 Tillman Pkwy, Grand Prairie, TX 75051
6417 Dorrance Way Dr, San Antonio, TX 78240
5920 Kessler Rd, Pasadena, TX 77504

Target Market(s)

1. Other physicians who might refer patients
2. Female patients

Industry/Entity Type

Business

Font styles to use
Other font styles liked:
• Tahoma for lettering

Requirements
Must have
• As per the instructions
Should not have
• No other images needed -- please try to keep font consistent with logo design. Can use Tahoma as the font for lettering.

```html
<!DOCTYPE html>
<html lang="en">
<head>
<meta charset="utf-8">
<title>Bright Pelvic Health – Business Card</title>
<link rel="stylesheet" href="https://fonts.googleapis.com/css2?family=Noto+Sans:wght@400;700&display=swap">
<style>
  :root {
    --backdrop: #ece9e4;
    --card-white: #ffffff;
    --brand-blue: #185aa0;
    --text-on-blue: #ffffff;
    --card-shadow: rgba(0, 0, 0, 0.28);
  }
  * { margin: 0; padding: 0; box-sizing: border-box; }
  html, body {
    width: 1200px;
    height: 1000px;
    overflow: hidden;
  }
  body {
    position: relative;
    background: var(--backdrop);
    font-family: "Noto Sans", Tahoma, sans-serif;
  }
  .card {
    position: absolute;
    width: 568px;
    height: 325px;
    background: var(--card-white);
    box-shadow: 0 6px 14px var(--card-shadow);
    display: flex;
    flex-direction: column;
  }
  .card--front { left: 190px; top: 122px; }
  .card--back  { left: 442px; top: 553px; }

  .card__brand {
    height: 153px;
    display: flex;
    align-items: flex-end;
    justify-content: center;
    padding-bottom: 30px;
  }
  .brand-name {
    color: var(--brand-blue);
    font-weight: 700;
    font-size: 25px;
    letter-spacing: 0.2px;
  }
  .card__panel {
    flex: 1;
    background: var(--brand-blue);
    color: var(--text-on-blue);
  }

  .physician-name {
    text-align: center;
    font-weight: 700;
    font-size: 30px;
    padding-top: 26px;
    line-height: 40px;
  }
  .contact-grid {
    display: grid;
    grid-template-columns: 256px 312px;
    margin-top: 26px;
    font-size: 15px;
    line-height: 23px;
  }
  .contact-grid__col { text-align: center; }

  .location-list {
    list-style: none;
    text-align: center;
    font-size: 15px;
    line-height: 21.8px;
    padding-top: 9px;
  }
</style>
</head>
<body>

  <section class="card card--front" aria-label="Business card front">
    <header class="card__brand">
      <span class="brand-name">Bright Pelvic Health</span>
    </header>
    <div class="card__panel">
      <h1 class="physician-name">Ravi K. Desai, MD FACOG</h1>
      <div class="contact-grid">
        <p class="contact-grid__col">phone: 469-555-0182<br>fax: 1-469-555-0147</p>
        <p class="contact-grid__col">email: admin@brightpelvic.example<br>website: www.brightpelvichealth.example</p>
      </div>
    </div>
  </section>

  <section class="card card--back" aria-label="Business card back">
    <header class="card__brand">
      <span class="brand-name">Bright Pelvic Health</span>
    </header>
    <div class="card__panel">
      <ul class="location-list">
        <li>4812 Quarry Bend Dr, Plano, TX 75093</li>
        <li>3650 Wrenfield Rd, Plano, TX 75025</li>
        <li>2245 Brambleton Ln, Irving, TX 75038</li>
        <li>915 S Garnet Ave B314, Dallas, TX 75201</li>
        <li>1836 Tillman Pkwy, Grand Prairie, TX 75051</li>
        <li>6417 Dorrance Way Dr, San Antonio, TX 78240</li>
        <li>5920 Kessler Rd, Pasadena, TX 77504</li>
      </ul>
    </div>
  </section>

</body>
</html>
```